Quiet Harbour is a Counseling company and needs a website design.

I need a website design for my Counseling company based in Singapore. I provide counseling and other related services through therapy. I website is my front face and want it to represent my personality and the name of the company itself. My company represents non judgement, compassionate and a safe environment for people to come by and talk about their issues/problems.

I want the website to be something connected to nature earth like a perfect Sanctuary. When a person sees my website i want to immediately feel a piece of calmness and peace. This is essential to me.

Target Market(s)

All age groups above 13 years of age

Industry/Entity Type

It Company

Requirements
Must have
• Not too flashy and must connect to any common man irrespective of age
Should not have
• Good calm color concept

```html
<!DOCTYPE html>
<html lang="en">
<head>
<meta charset="utf-8">
<title>Quiet Harbour — Counseling</title>
<link href="https://fonts.googleapis.com/css2?family=Cutive+Mono&display=swap" rel="stylesheet">
<style>
  :root {
    --sky-top: #5fa8d8;
    --sky-light: #cfe6f2;
    --leaf: #4e8f2e;
    --leaf-light: #8cc048;
    --water: #1b9fb3;
    --water-deep: #0b4a5a;
    --bar: rgba(20, 40, 50, 0.72);
    --dropdown: rgba(70, 80, 85, 0.78);
    --nav-text: #ffffff;
    --body-text: #1c1f1f;
    --dot: rgba(255, 255, 255, 0.55);
    --dot-active: #ffffff;
  }
  * { margin: 0; padding: 0; box-sizing: border-box; }
  html, body { width: 1200px; height: 775px; overflow: hidden; }
  body {
    position: relative;
    font-family: "Cutive Mono", "Courier New", monospace;
    font-variant: small-caps;
  }
  .hero-scene {
    position: absolute; inset: 0;
    background: linear-gradient(180deg,
      var(--sky-top) 0%,
      var(--sky-light) 22%,
      var(--leaf-light) 45%,
      var(--leaf) 60%,
      var(--water) 72%,
      var(--water-deep) 100%);
  }
  .top-bar {
    position: absolute; top: 0; left: 0; right: 0; height: 47px;
    background: var(--bar);
    color: var(--nav-text);
    font-size: 16px; letter-spacing: 0.5px;
  }
  .brand { position: absolute; left: 47px; top: 14px; }
  .main-nav {
    position: absolute; right: 51px; top: 14px;
    display: flex; gap: 7px; list-style: none;
  }
  .main-nav li { position: relative; }
  .main-nav .sep { opacity: 0.9; }
  .main-nav .current { text-decoration: underline; text-underline-offset: 3px; }
  .dropdown {
    position: absolute; left: 790px; top: 47px;
    width: 137px; height: 45px;
    background: var(--dropdown);
    color: #e4e8e8; font-size: 13px;
    padding: 5px 11px; line-height: 19px;
    list-style: none;
  }
  .dropdown li.active { border-bottom: 1px solid #e4e8e8; }
  .content {
    position: absolute; left: 259px; top: 130px; width: 500px;
    color: var(--body-text);
  }
  .content h1 {
    font-weight: 400; font-size: 30px; letter-spacing: 1px;
    margin-bottom: 22px;
  }
  .content p {
    font-size: 19px; line-height: 26px; text-indent: 20px;
    margin-bottom: 26px;
  }
  .slider-dots {
    position: absolute; left: 937px; top: 695px;
    display: flex; gap: 12px; list-style: none;
  }
  .slider-dots li {
    width: 8px; height: 8px; border-radius: 50%; background: var(--dot);
  }
  .slider-dots li.active { background: var(--dot-active); border: 2px solid #333; }
  .footer-band {
    position: absolute; left: 0; right: 0; top: 729px; bottom: 0;
    background: rgba(5, 30, 40, 0.6);
  }
</style>
</head>
<body>
  <div class="hero-scene" role="img" aria-label="Photograph of a calm turquoise lake framed by green forested hills and sunlit leaves under a bright blue sky"></div>

  <header class="top-bar">
    <div class="brand">Quiet Harbour</div>
    <ul class="main-nav">
      <li>Home</li><li class="sep">/</li>
      <li class="current">About</li><li class="sep">/</li>
      <li>Consultation</li><li class="sep">/</li>
      <li>Resources</li><li class="sep">/</li>
      <li>Contact</li>
    </ul>
  </header>

  <ul class="dropdown">
    <li>-About me</li>
    <li class="active">-Quiet Harbour</li>
  </ul>

  <main class="content">
    <h1>Quiet Harbour</h1>
    <p>Lorem ipsum dolor sit amet, consectetur adipiscing elit. Praesent ullamcorper interdum faucibus. Aenean vel tellus porta, luctus urna eu, ornare felis. Nulla accumsan, nisi in sodales faucibus, elit neque scelerisque sem, elementum interdum enim dui vitae justo. In commodo ipsum in vestibulum pretium. In non nisi enim. Ut laoreet sapien nisi, sed dapibus lectus porttitor vitae.</p>
    <p>Aliquam sagittis enim sodales, venenatis nibh ac, imperdiet justo. Nullam dolor nisi, viverra ac pretium sed, pulvinar eu neque. Curabitur mattis metus eros. Aenean faucibus, magna eget porttitor suscipit, mauris nisi semper lectus, dictum elementum metus elit</p>
  </main>

  <ul class="slider-dots">
    <li class="active"></li><li></li><li></li><li></li><li></li>
  </ul>

  <div class="footer-band"></div>
</body>
</html>
```